依頼概要
■依頼の目的/概要
和歌山県で自然農法の農家をしています「坂口青葉ファーム」と申します。
弊社が販売している「大麦シリアル」のラベルデザインをお願いします。

■依頼詳細
今回は弊社が販売する自然農法の「大麦シリアル」のラベルのデザインをお願いします。

特徴
●原材料の大麦は、完全無肥料・無農薬の自然農法栽培のものを100%使用していますので健康志向の方にお勧めで安心して食べて頂けます。
●全て自社「坂口青葉ファーム」産の六条大麦を使用しています。
●今話題になっている、五穀の王様である「大麦」が毎日手軽に食べられるシリアルになりました。
●朝食やおやつなどに手軽に食べれて健康的です。
●牛乳・豆乳・ヨーグルトなどをかけて食べて頂けます。
●お好みで果物やドライフルーツ、ナッツなどを添えて食べると更に健康的です。
●何もかけずにポン菓子のようにも食べることができます。砂糖などで甘味を付けていないのでお子様のおやつにも安心です。
●大麦は水溶性食物繊維が豊富でとても体にいい食べ物です。

■その他要望
●自社のロゴマークをラベルデザインの中にいれてください。
ロゴマークは添付してあります。
●パッケージは
透明のスタンドチャック式のものです。(表面透明、裏面は白)
大きさはチャックの部分まで含めて
縦230㎜×横160㎜になります。(添付写真あります)
●添付写真に大麦シリアルの写真があります。使えそうなら使って下さい。
独自の写真を使って頂いても結構です。

●表記に関してですが
「無肥料・無農薬」とは法律上書くことができません。
「無肥料・無農薬」×→「肥料・農薬不使用」○と表記してください。
「自然農法」という言葉も登録商標の関係で使えません。
「自然農法」×→「自然栽培」とお願いします。
●朝から健康のために続けたくなるようなデザインをお願いいたします。
デザイナーの皆様、どうぞよろしくお願いいたします。

その他何かご不明な点がございましたら、お気軽にご質問下さい。
よろしくお願いいたします。
■ 選んだ理由

バランスが取れていて分かりやすい
必要な説明が明記されている
写真を効果的に使っている

■ 提案者全員のお礼・コメント

素晴らしいご提案を頂きありがとうございました。
今後ともどうぞよろしくお願いします。

```html
<!DOCTYPE html>
<html lang="ja">
<head>
<meta charset="utf-8">
<title>大麦シリアル ラベル</title>
<link rel="stylesheet" href="https://fonts.googleapis.com/css2?family=Shippori+Mincho+B1:wght@500;800&family=Cormorant+Garamond:wght@600&display=swap">
<style>
  :root {
    --bg: #ffffff;
    --pouch-clear: #eef0f0;
    --pouch-edge: #d6d9da;
    --grain-light: #d9c6a3;
    --grain-mid: #b89d74;
    --grain-dark: #8f7654;
    --ink: #2a2116;
    --ink-soft: #3b3126;
    --gold: #d1a93c;
    --gold-deep: #b48a22;
  }
  html, body {
    margin: 0;
    width: 797px;
    height: 1200px;
    overflow: hidden;
    background: var(--bg);
  }
  .canvas {
    position: relative;
    width: 797px;
    height: 1200px;
  }
  .pouch {
    position: absolute;
    left: 58px;
    top: 27px;
    width: 692px;
    height: 1143px;
    background: var(--pouch-clear);
    border: 2px solid var(--pouch-edge);
    border-radius: 10px 10px 4px 4px;
    overflow: hidden;
  }
  .pouch__zipper {
    position: absolute;
    left: 0;
    right: 0;
    top: 72px;
    height: 6px;
    background: var(--pouch-edge);
  }
  .pouch__contents {
    position: absolute;
    left: 28px;
    right: 28px;
    top: 150px;
    bottom: 40px;
    border-radius: 40px 40px 12px 12px;
    background: radial-gradient(ellipse at 50% 45%, var(--grain-light) 0%, var(--grain-mid) 70%, var(--grain-dark) 100%);
  }
  .label {
    position: absolute;
    inset: 0;
  }
  .label__wreath {
    position: absolute;
    left: 168px;
    top: 478px;
    width: 374px;
    height: 340px;
    border-radius: 50%;
    background: radial-gradient(circle, transparent 58%, var(--gold) 60%, var(--gold-deep) 68%, transparent 72%);
    opacity: 0.9;
  }
  .label__title {
    position: absolute;
    left: 306px;
    top: 400px;
    writing-mode: vertical-rl;
    font-family: "Shippori Mincho B1", serif;
    font-weight: 800;
    font-size: 68px;
    letter-spacing: 0.02em;
    color: var(--ink);
    margin: 0;
    line-height: 1;
  }
  .label__method {
    position: absolute;
    left: 456px;
    top: 410px;
    writing-mode: vertical-rl;
    font-family: "Shippori Mincho B1", serif;
    font-weight: 500;
    font-size: 30px;
    letter-spacing: 0.12em;
    color: var(--ink-soft);
    margin: 0;
  }
  .label__claim {
    position: absolute;
    left: 262px;
    top: 530px;
    writing-mode: vertical-rl;
    font-family: "Shippori Mincho B1", serif;
    font-weight: 500;
    font-size: 24px;
    letter-spacing: 0.06em;
    color: var(--ink-soft);
    margin: 0;
  }
  .label__brand {
    position: absolute;
    left: 0;
    right: 0;
    top: 810px;
    text-align: center;
    font-family: "Cormorant Garamond", serif;
    font-weight: 600;
    font-size: 24px;
    letter-spacing: 0.18em;
    color: var(--ink-soft);
  }
  .label__farm {
    position: absolute;
    left: 0;
    right: 0;
    top: 846px;
    text-align: center;
    font-family: "Shippori Mincho B1", serif;
    font-weight: 500;
    font-size: 16px;
    letter-spacing: 0.1em;
    color: var(--ink-soft);
  }
</style>
</head>
<body>
<main class="canvas">
  <div class="pouch">
    <div class="pouch__zipper"></div>
    <div class="pouch__contents" role="img" aria-label="袋の中に見える大麦シリアルの粒"></div>
    <div class="label">
      <div class="label__wreath" role="img" aria-label="金色の麦の穂で囲んだ輪飾り"></div>
      <h1 class="label__title">大麦シリアル</h1>
      <p class="label__method">自然栽培</p>
      <p class="label__claim">肥料・農薬不使用</p>
      <div class="label__brand">AOBA</div>
      <div class="label__farm">坂口青葉ファーム</div>
    </div>
  </div>
</main>
</body>
</html>
```